Business Card design for law firm = Juriskite Australia

We are seeking a new design for our business cards.
We are keeping our logo, which is attached.
We need space for
Name
Title
Address is , which is
Level 14
82 Penhallow Street
Sydney NSW 2000
Phone :
Mobile :
Fax :
Email :
DX :
website www.juriskite.com.au

Industry/Entity Type

Law Firm / Banking and Finance

Contact Information for Business Card

We are seeking a new design for our business cards. We are keeping our logo. We need space for Name Title Address is Level 14 82 Penhallow Street Sydney NSW 2000 Phone Mobile Fax Email DX website www.juriskite.com.au

Colors
0054AA
0677BA
7BADD7
CADEEF
E8F1F8

Requirements
Must have
• see our website for general feel www.juriskite.com.au

```html
<!DOCTYPE html>
<html lang="en">
<head>
<meta charset="utf-8">
<title>Juriskite Australia – Business Card</title>
<link href="https://fonts.googleapis.com/css2?family=Mulish:wght@400;700&display=swap" rel="stylesheet">
<style>
  :root {
    --backdrop: #ababab;
    --paper: #ffffff;
    --brand-blue: #1b62ab;
    --rule-teal: #1a9ac8;
    --ink: #4a4a4a;
    --white: #ffffff;
  }
  * { box-sizing: border-box; margin: 0; padding: 0; }
  html, body {
    width: 1200px; height: 1000px; overflow: hidden;
    background: var(--backdrop);
    font-family: "Mulish", sans-serif;
  }
  .canvas { position: relative; width: 1200px; height: 1000px; }
  .card { position: absolute; width: 515px; height: 297px; left: 341px; }
  .card--front { top: 146px; background: var(--paper); }
  .card--back { top: 516px; background: var(--brand-blue); }

  .brand-name { position: absolute; font-weight: 400; white-space: nowrap; }
  .card--front .brand-name { left: 42px; top: 78px; font-size: 22px; color: var(--brand-blue); }

  .person { position: absolute; left: 37px; top: 154px; }
  .person__name { font-size: 17px; font-weight: 700; color: var(--brand-blue); }
  .person__title { font-size: 13px; color: var(--ink); margin-top: 3px; margin-left: 1px; letter-spacing: .2px; }

  .divider { position: absolute; left: 39px; top: 202px; width: 438px; height: 2px; background: var(--rule-teal); }

  .contact-list, .address { position: absolute; list-style: none; font-size: 12.5px; line-height: 15.7px; color: var(--ink); }
  .contact-list { left: 39px; top: 217px; }
  .contact-list li { display: flex; align-items: center; gap: 6px; }
  .icon { width: 12px; height: 12px; fill: var(--brand-blue); flex: none; }
  .address { left: 284px; top: 217px; display: flex; gap: 4px; }
  .address .icon { margin-top: 2px; }

  .card--back .brand-name { left: 0; width: 515px; text-align: center; top: 140px; font-size: 44px; color: var(--white); }
  .website { position: absolute; left: 173px; top: 247px; display: flex; align-items: center; gap: 5px; font-size: 12.5px; color: var(--white); }
  .website .icon { fill: none; stroke: var(--white); stroke-width: 1.3; }
</style>
</head>
<body>
<main class="canvas">
  <section class="card card--front" aria-label="Card front">
    <div class="brand-name">Juriskite</div>

    <div class="person">
      <p class="person__name">Maren Holloway</p>
      <p class="person__title">Chief Legal Officer</p>
    </div>

    <div class="divider"></div>

    <ul class="contact-list">
      <li><svg class="icon" viewBox="0 0 12 12"><path d="M2.5 0.8 4.6 3 3.5 4.3c.7 1.6 2.5 3.4 4.2 4.2L9 7.4l2.2 2.1-1.3 1.7C5.3 11 1 6.7.8 2.1z"/></svg>02 9876 0145</li>
      <li><svg class="icon" viewBox="0 0 12 12"><path d="M3 .5h6v3H3zM1 4h10v5H9v2.5H3V9H1zM4 7v3.5h4V7z"/></svg>02 9876 0146</li>
      <li><svg class="icon" viewBox="0 0 12 12"><path d="M.5 2.5h11v7H.5zM1.5 3.3 6 6.6l4.5-3.3" stroke="#fff" stroke-width=".9"/></svg>enquiries@juriskite.com.au</li>
    </ul>

    <div class="address">
      <svg class="icon" viewBox="0 0 12 12"><path d="M6 .3a4 4 0 0 0-4 4c0 3 4 7.4 4 7.4s4-4.4 4-7.4a4 4 0 0 0-4-4zm0 5.6a1.6 1.6 0 1 1 0-3.2 1.6 1.6 0 0 1 0 3.2z"/></svg>
      <p>Level 14, 82 Penhallow Street,<br>Sydney NSW 2000<br>DX 321 Sydney</p>
    </div>
  </section>

  <section class="card card--back" aria-label="Card back">
    <div class="brand-name">Juriskite</div>
    <p class="website">
      <svg class="icon" viewBox="0 0 12 12"><circle cx="6" cy="6" r="5.2"/><ellipse cx="6" cy="6" rx="2.3" ry="5.2"/><path d="M.8 6h10.4M1.6 3.4h8.8M1.6 8.6h8.8"/></svg>
      www.juriskite.com.au
    </p>
  </section>
</main>
</body>
</html>
```